Graphic design of labels for scented candles

Following a change in our team structure, a deadline was put in place and the brief changed.
We need a beautiful label for our candles, one that sticks *all around the glass*. Must obviously include our logo as well as the description of the perfume.
The clientele is mainly female, between 35 and 65 years old, of a classic nature.
Brand values:
Feminine
Warm-joyful
Sophisticated-elegant
Eco-friendly, pet-friendly
Natural
Inspires confidence.
The idea is to have something different, the final appearance must be elegant and refined, which will be your challenge given the shape.

What we need:
- changeable colors
- small transparent elements which can be printed on a gold or silver paper background (example: logo, frame, elements, etc.)

- the logo (black or very dark gray) must be present + text "vegetable candle", then the perfume and below:
vegetable wax - handcrafted"
I am attaching a picture of our current labels to the files.
For the size I'll let you manage.
These labels can also be assigned to derived products such as room fragrances, pillow mists, etc.
The brand targets the middle class and above.
For the fonts I leave the choice to you.
Thank you and good luck to all !

Update: there is no longer a cat's head as a background shape, you have free choice.
THANKS

Target Market(s)

Women aged 35 to 65

Industry/Entity Type

Industrie du Parfum

Colors
00AB8E
00BBA5
67D7C9
C6EFE9
E9F9F6
59FF00
82FF00
B8FF75
E3FFCB
F4FFEA
FFF300
FFF600
FEFA6F
FFFEC7
FFFEE8
FFC000
F8CF3A
FAE287
FDF2CF
FEFAEE
F0912C
F2A743
F7CA91
FBE8D2
FDF5EE
EE7325
F08F49
F5BC92
FAE3D3
FDF4ED
EB3D1F
EC4F4E
F09395
F8D3D4
FCEDEE
E54698
E96AAD
F1A4CE
F9D9EA
FCEFF6
A7469A
B969AE
D3A5CF
EDDBEB
F8F0F9
6B429C
8869AF
B7A5CE
E3DAEB
F3F0F8

Requirements
Must have
• modifiable colors - small transparent elements which can be printed on a gold or silver paper background (example: frame, elements, etc.) - the logo (black or very dark gray) must be present + text "vegetable candle, then the perfume and below: vegetable wax - handcrafted"
Nice to have
• Elements that could be made transparent (logo text frame) to be able to edit on gold papers and give a luxurious appearance
Should not have
• no childish appearance.

```html
<!DOCTYPE html>
<html lang="en">
<head>
<meta charset="utf-8">
<title>Velours Candle – Label Range</title>
<link href="https://fonts.googleapis.com/css2?family=Montserrat:wght@500;700&family=Great+Vibes&display=swap" rel="stylesheet">
<style>
  :root{
    --teal:#6cc9c0;
    --teal-tint:#e6f6f4;
    --pink:#e46aaf;
    --pink-tint:#fbe8f2;
    --mono-tint:#ececec;
    --ink:#111111;
    --paper:#ffffff;
    --page:#ffffff;
  }
  *{box-sizing:border-box;margin:0;padding:0}
  html,body{width:887px;height:1200px;overflow:hidden;background:var(--page)}
  .sheet{position:relative;width:887px;height:1200px}

  .label{position:absolute;width:412px;height:273px;transform-origin:0 0}
  .label-shape{position:absolute;inset:0;width:100%;height:100%}
  .label--teal{--accent:var(--teal)}
  .label--pink{--accent:var(--pink)}

  .panel{
    position:absolute;left:110px;top:25px;width:192px;height:224px;
    background:var(--paper);
    display:flex;flex-direction:column;align-items:center;
    padding-top:38px;text-align:center;color:var(--ink);
  }
  .panel--black{border:2px solid var(--ink)}
  .panel--accent{border:2px solid var(--accent)}
  .panel--double-black{border:1.5px solid var(--ink);outline:1.5px solid var(--ink);outline-offset:3px}
  .panel--double-accent{border:1.5px solid var(--accent);outline:1.5px solid var(--accent);outline-offset:3px}

  .brand-name{
    font-family:"Montserrat",sans-serif;font-weight:700;font-size:27px;
    letter-spacing:.5px;color:var(--ink);line-height:1;
    display:flex;align-items:center;gap:5px;
  }
  .brand-dot{width:7px;height:7px;border-radius:50%;background:var(--ink)}
  .brand-line{
    display:flex;align-items:center;gap:4px;margin-top:5px;
    font-family:"Montserrat",sans-serif;font-weight:500;font-size:9px;letter-spacing:4px;
  }
  .brand-line::before,.brand-line::after{content:"";width:18px;height:1px;background:var(--ink)}
  .brand-url{font-family:"Montserrat",sans-serif;font-weight:700;font-size:8px;margin-top:2px}
  .wax-note{font-family:"Great Vibes",cursive;font-size:14px;margin-top:16px}
  .perfume{font-family:"Great Vibes",cursive;font-size:27px;color:var(--accent);margin-top:8px;line-height:1}
  .product-type{font-family:"Great Vibes",cursive;font-size:14px;margin-top:10px}
</style>
</head>
<body>
<main class="sheet">

  <!-- Row 1 -->
  <section class="label label--teal" style="left:21px;top:7px">
    <svg class="label-shape" viewBox="0 0 412 273" preserveAspectRatio="none" role="img" aria-label="Label shape filled with a small fruit and flower pattern in teal">
      <path d="M16,30 Q206,-4 396,30 L404,150 Q398,245 206,270 Q14,245 8,150 Z" fill="var(--teal-tint)" stroke="var(--teal)" stroke-width="4"/>
    </svg>
    <div class="panel panel--black">
      <div class="brand-name"><span class="brand-dot"></span>velours</div>
      <div class="brand-line">CANDLE</div>
      <div class="brand-url">www.velours-candle.com</div>
      <div class="wax-note">vegetable wax – handcrafted</div>
      <div class="perfume">Mangue et Papaye</div>
      <div class="product-type">vegetable candle</div>
    </div>
  </section>

  <section class="label label--teal" style="left:451px;top:7px">
    <svg class="label-shape" viewBox="0 0 412 273" preserveAspectRatio="none" role="img" aria-label="Label shape filled with a small black fruit and flower pattern">
      <path d="M16,30 Q206,-4 396,30 L404,150 Q398,245 206,270 Q14,245 8,150 Z" fill="var(--mono-tint)" stroke="var(--teal)" stroke-width="4"/>
    </svg>
    <div class="panel panel--accent">
      <div class="brand-name"><span class="brand-dot"></span>velours</div>
      <div class="brand-line">CANDLE</div>
      <div class="brand-url">www.velours-candle.com</div>
      <div class="wax-note">vegetable wax – handcrafted</div>
      <div class="perfume">Mangue et Papaye</div>
      <div class="product-type">vegetable candle</div>
    </div>
  </section>

  <!-- Row 2 -->
  <section class="label label--pink" style="left:21px;top:312px">
    <svg class="label-shape" viewBox="0 0 412 273" preserveAspectRatio="none" role="img" aria-label="Label shape filled with a small fruit and flower pattern in pink">
      <path d="M16,30 Q206,-4 396,30 L404,150 Q398,245 206,270 Q14,245 8,150 Z" fill="var(--pink-tint)" stroke="var(--pink)" stroke-width="4"/>
    </svg>
    <div class="panel panel--double-black">
      <div class="brand-name"><span class="brand-dot"></span>velours</div>
      <div class="brand-line">CANDLE</div>
      <div class="brand-url">www.velours-candle.com</div>
      <div class="wax-note">vegetable wax – handcrafted</div>
      <div class="perfume">Mangue et Papaye</div>
      <div class="product-type">vegetable candle</div>
    </div>
  </section>

  <section class="label label--pink" style="left:451px;top:312px">
    <svg class="label-shape" viewBox="0 0 412 273" preserveAspectRatio="none" role="img" aria-label="Label shape filled with a small black fruit and flower pattern">
      <path d="M16,30 Q206,-4 396,30 L404,150 Q398,245 206,270 Q14,245 8,150 Z" fill="var(--mono-tint)" stroke="var(--pink)" stroke-width="4"/>
    </svg>
    <div class="panel panel--double-accent">
      <div class="brand-name"><span class="brand-dot"></span>velours</div>
      <div class="brand-line">CANDLE</div>
      <div class="brand-url">www.velours-candle.com</div>
      <div class="wax-note">vegetable wax – handcrafted</div>
      <div class="perfume">Mangue et Papaye</div>
      <div class="product-type">vegetable candle</div>
    </div>
  </section>

  <!-- Row 3: applied sizes -->
  <section class="label label--pink" style="left:53px;top:788px;transform:scale(.785)">
    <svg class="label-shape" viewBox="0 0 412 273" preserveAspectRatio="none" role="img" aria-label="Label shape filled with a small black fruit and flower pattern">
      <path d="M16,30 Q206,-4 396,30 L404,150 Q398,245 206,270 Q14,245 8,150 Z" fill="var(--mono-tint)" stroke="var(--pink)" stroke-width="4"/>
    </svg>
    <div class="panel panel--double-accent">
      <div class="brand-name"><span class="brand-dot"></span>velours</div>
      <div class="brand-line">CANDLE</div>
      <div class="brand-url">www.velours-candle.com</div>
      <div class="wax-note">vegetable wax – handcrafted</div>
      <div class="perfume">Mangue et Papaye</div>
      <div class="product-type">vegetable candle</div>
    </div>
  </section>

  <section class="label label--pink" style="left:490px;top:845px;transform:scale(.785)">
    <svg class="label-shape" viewBox="0 0 412 273" preserveAspectRatio="none" role="img" aria-label="Label shape filled with a small fruit and flower pattern in pink">
      <path d="M16,30 Q206,-4 396,30 L404,150 Q398,245 206,270 Q14,245 8,150 Z" fill="var(--pink-tint)" stroke="var(--pink)" stroke-width="4"/>
    </svg>
    <div class="panel panel--double-black">
      <div class="brand-name"><span class="brand-dot"></span>velours</div>
      <div class="brand-line">CANDLE</div>
      <div class="brand-url">www.velours-candle.com</div>
      <div class="wax-note">vegetable wax – handcrafted</div>
      <div class="perfume">Mangue et Papaye</div>
      <div class="product-type">vegetable candle</div>
    </div>
  </section>

</main>
</body>
</html>
```